Postcard Design

The Amberly Courier ~ Your #1 Newspaper since 1971

I am trying to reach new clients with our special of
Receive 1 month free with a year contract.

The Amberly Courier is a monthly newspaper that readers cherish like a magazine waiting for the next one to be published. I have had several advertisers since the first paper in 1971. My mom was the prior owner and she loved roosters, hence the rooster in the logo.

Please add the following:

Your # 1 Newspaper 

Serving Hollin County since 1971

1 Month FREE with 1 Year Contract

Instead of your #1 Newspaper...please put

The areas best place to see what's happening locally.

Target Market(s)

professionals, restaurants, etc.

Colors
33b7a4
85cae6
33a6d7

Requirements
Must have
• P.O. Box 417, Westbrook Mills, NJ 08652
Email: info@amberlycourier-example.com
609.555.0148
www.amberlycourier-example.com
Nice to have
• Typical savings up to $300.

```html
<!DOCTYPE html>
<html lang="en">
<head>
<meta charset="utf-8">
<title>The Amberly Courier – Postcard</title>
<link rel="stylesheet" href="https://fonts.googleapis.com/css2?family=Source+Sans+3:wght@400;700&display=swap">
<style>
  :root {
    --paper: #ffffff;
    --ink: #111111;
    --teal: #33b7a4;
    --sky: #85cae6;
    --ocean: #33a6d7;
  }
  html, body {
    margin: 0;
    padding: 0;
    width: 1200px;
    height: 930px;
    overflow: hidden;
    background: var(--paper);
  }
  .postcard {
    position: relative;
    width: 1200px;
    height: 930px;
    background: var(--paper);
    color: var(--ink);
    font-family: "Source Sans 3", "Myriad Pro", Arial, sans-serif;
    font-weight: 400;
  }
  .masthead-name {
    position: absolute;
    left: 58px;
    top: 46px;
    margin: 0;
    font-size: 50px;
    line-height: 1;
    font-weight: 400;
    white-space: nowrap;
  }
  .return-address {
    position: absolute;
    left: 72px;
    top: 118px;
    margin: 0;
    font-style: normal;
    font-size: 29px;
    line-height: 39.5px;
  }
  .return-address span {
    display: block;
    white-space: nowrap;
  }
  .promo {
    position: absolute;
    left: 72px;
    right: 72px;
    top: 360px;
  }
  .promo-rule {
    height: 6px;
    background: linear-gradient(90deg, var(--teal), var(--sky), var(--ocean));
    margin-bottom: 34px;
  }
  .tagline {
    margin: 0 0 14px;
    font-size: 36px;
    line-height: 1.2;
    color: var(--ocean);
    white-space: nowrap;
  }
  .serving-line {
    margin: 0 0 40px;
    font-size: 30px;
    line-height: 1.2;
    color: var(--teal);
    white-space: nowrap;
  }
  .offer {
    background: var(--sky);
    padding: 30px 36px;
  }
  .offer-headline {
    margin: 0 0 10px;
    font-size: 54px;
    line-height: 1.1;
    font-weight: 700;
    color: var(--ink);
    white-space: nowrap;
  }
  .offer-savings {
    margin: 0;
    font-size: 30px;
    line-height: 1.2;
    color: var(--ink);
    white-space: nowrap;
  }
</style>
</head>
<body>
  <main class="postcard">
    <h1 class="masthead-name">The Amberly Courier</h1>
    <address class="return-address">
      <span class="address-line">P.O. Box 417, Westbrook Mills, NJ 08652</span>
      <span class="email-line">Email: info@amberlycourier-example.com</span>
      <span class="phone-line">609.555.0148</span>
      <span class="web-line">www.amberlycourier-example.com</span>
    </address>
    <section class="promo">
      <div class="promo-rule"></div>
      <p class="tagline">The area's best place to see what's happening locally.</p>
      <p class="serving-line">Serving Hollin County since 1971</p>
      <div class="offer">
        <p class="offer-headline">1 Month FREE with 1 Year Contract</p>
        <p class="offer-savings">Typical savings up to $300.</p>
      </div>
    </section>
  </main>
</body>
</html>
```